Client Proposal

I need a proposal template to give to potential clients detailing our services, safety, company history, table of contents and appendixes. I need a cover page to start with images describing our services. Our company is based in Grande Prairie, Alberta. We do land survey work, engineering and environmental.

In word format please so that we can change the proposal on an as needed basis.

```html
<!DOCTYPE html>
<html lang="en">
<head>
<meta charset="utf-8">
<title>Northline Group – Business Proposal Folder</title>
<link rel="stylesheet" href="https://fonts.googleapis.com/css2?family=Open+Sans:wght@400;600;700;800&family=Caladea:wght@400;700&display=swap">
<style>
  :root {
    --stage: #e4e5e7;
    --brand-blue: #1f97cf;
    --back-blue-dark: #2a7fa3;
    --back-blue-light: #389fcb;
    --slate-grey: #7b7f83;
    --text-grey: #6a6a6a;
    --text-dark: #222222;
    --link-blue: #2b2bd0;
    --paper: #ffffff;
    --photo-tone-a: #a4947a;
    --photo-tone-b: #988466;
  }
  * { margin: 0; padding: 0; box-sizing: border-box; }
  html, body { width: 1200px; height: 793px; overflow: hidden; }
  body {
    background: var(--stage);
    position: relative;
    font-family: "Open Sans", sans-serif;
  }
  .page {
    position: absolute;
    top: 34px;
    width: 560px;
    height: 725px;
    box-shadow: 0 6px 18px rgba(0,0,0,0.18);
  }
  .back-cover {
    left: 40px;
    background: linear-gradient(90deg, var(--back-blue-dark) 0%, var(--back-blue-light) 55%, var(--back-blue-dark) 100%);
  }
  .front-cover {
    left: 600px;
    background: var(--paper);
    overflow: hidden;
  }
  .brand {
    position: absolute;
    left: 30px;
    top: 38px;
  }
  .brand-name {
    display: flex;
    align-items: center;
    gap: 8px;
    font-weight: 700;
    font-size: 21px;
    color: var(--brand-blue);
    letter-spacing: 0.5px;
  }
  .brand-mark {
    width: 16px;
    height: 16px;
    background: var(--slate-grey);
  }
  .brand-tagline {
    margin-top: 2px;
    padding-left: 24px;
    font-size: 9.5px;
    font-weight: 600;
    color: var(--slate-grey);
  }
  .offices {
    position: absolute;
    left: 330px;
    top: 22px;
    width: 215px;
    font-family: "Caladea", serif;
    font-size: 10.5px;
    line-height: 1.3;
    color: var(--text-grey);
  }
  .office + .office { margin-top: 8px; }
  .office-title {
    font-family: "Open Sans", sans-serif;
    font-weight: 700;
    font-size: 12.5px;
    color: var(--brand-blue);
  }
  .office-line { padding-left: 4px; }
  .office-contact {
    display: flex;
    align-items: center;
    gap: 5px;
    padding-left: 10px;
  }
  .office-contact svg { flex: none; }
  .phone { color: var(--text-dark); }
  .email { color: var(--link-blue); text-decoration: underline; }
  .title-band {
    position: absolute;
    left: 0;
    top: 262px;
    width: 560px;
    height: 140px;
  }
  .title-text {
    position: absolute;
    left: 48px;
    top: 312px;
    font-weight: 800;
    font-size: 30px;
    color: var(--paper);
    letter-spacing: 0.3px;
  }
  .cover-photo {
    position: absolute;
    left: 0;
    top: 412px;
    width: 560px;
    height: 232px;
    background: linear-gradient(135deg, var(--photo-tone-a) 0%, var(--photo-tone-b) 100%);
  }
  .footer-strip {
    position: absolute;
    left: 0;
    top: 644px;
    width: 560px;
    height: 81px;
    background: linear-gradient(180deg, #ececec 0%, var(--paper) 45%);
  }
  .website {
    position: absolute;
    right: 70px;
    top: 672px;
    font-size: 13.5px;
    color: var(--slate-grey);
    letter-spacing: 0.3px;
  }
  .website-domain { color: var(--brand-blue); }
</style>
</head>
<body>
  <div class="page back-cover"></div>

  <div class="page front-cover">
    <div class="brand">
      <div class="brand-name"><span class="brand-mark"></span>NORTHLINE GROUP</div>
      <div class="brand-tagline">Surveying &amp; Engineering</div>
    </div>

    <div class="offices">
      <div class="office">
        <div class="office-title">Ridgeview Office</div>
        <div class="office-line">Unit 210, 4500 Sample Road</div>
        <div class="office-line">Ridgeview, AB A1A 1A1</div>
        <div class="office-contact phone">
          <svg width="9" height="8" viewBox="0 0 9 8"><path d="M0 2 Q4.5 -1 9 2 L8 3.5 L6.5 3 L6.5 2 Q4.5 1.2 2.5 2 L2.5 3 L1 3.5 Z M1.5 4 H7.5 V8 H1.5 Z" fill="#1f97cf"/></svg>
          555-010-1234
        </div>
        <div class="office-contact">
          <svg width="10" height="7" viewBox="0 0 10 7"><rect x="0.5" y="0.5" width="9" height="6" fill="none" stroke="#1f97cf"/><path d="M0.5 0.5 L5 4 L9.5 0.5" fill="none" stroke="#1f97cf"/></svg>
          <span class="email">dana@northlinegroup.example</span>
        </div>
      </div>
      <div class="office">
        <div class="office-title">Elk Bend Office</div>
        <div class="office-line">#5, 1200 Example Street</div>
        <div class="office-line">Elk Bend, AB B2B 2B2</div>
        <div class="office-contact phone">
          <svg width="9" height="8" viewBox="0 0 9 8"><path d="M0 2 Q4.5 -1 9 2 L8 3.5 L6.5 3 L6.5 2 Q4.5 1.2 2.5 2 L2.5 3 L1 3.5 Z M1.5 4 H7.5 V8 H1.5 Z" fill="#1f97cf"/></svg>
          555-010-5678
        </div>
        <div class="office-contact">
          <svg width="10" height="7" viewBox="0 0 10 7"><rect x="0.5" y="0.5" width="9" height="6" fill="none" stroke="#1f97cf"/><path d="M0.5 0.5 L5 4 L9.5 0.5" fill="none" stroke="#1f97cf"/></svg>
          <span class="email">reid@northlinegroup.example</span>
        </div>
      </div>
      <div class="office">
        <div class="office-title">Maple Hollow Office</div>
        <div class="office-line">3300 Placeholder Street</div>
        <div class="office-line">Maple Hollow, AB C3C 3C3</div>
        <div class="office-contact phone">
          <svg width="9" height="8" viewBox="0 0 9 8"><path d="M0 2 Q4.5 -1 9 2 L8 3.5 L6.5 3 L6.5 2 Q4.5 1.2 2.5 2 L2.5 3 L1 3.5 Z M1.5 4 H7.5 V8 H1.5 Z" fill="#1f97cf"/></svg>
          555-010-9012
        </div>
        <div class="office-contact">
          <svg width="10" height="7" viewBox="0 0 10 7"><rect x="0.5" y="0.5" width="9" height="6" fill="none" stroke="#1f97cf"/><path d="M0.5 0.5 L5 4 L9.5 0.5" fill="none" stroke="#1f97cf"/></svg>
          <span class="email">sam@northlinegroup.example</span>
        </div>
      </div>
    </div>

    <svg class="title-band" viewBox="0 0 560 140" aria-hidden="true">
      <polygon points="0,8 452,0 420,140 0,140" fill="var(--brand-blue)"/>
      <polygon points="462,0 560,0 560,124 430,136" fill="var(--slate-grey)"/>
    </svg>
    <h1 class="title-text">Business Proposal</h1>

    <div class="cover-photo" role="img" aria-label="Photo of a land surveyor in a hard hat and safety vest operating a total station on a tripod in open foothills country"></div>

    <div class="footer-strip"></div>
    <div class="website">www.<span class="website-domain">northlinegroup</span>.example</div>
  </div>
</body>
</html>
```